I'm doing a recreational cannabis grow business here in the Columbia Gorge scenic area . I'm looking for a business card similar to the Tarvelle Lodge logo,except for the sun raise to be pot leafs.
The Gorge mountains,the river with the sun coming off the water between the mountains with the pot leaf rays.
All print would be on the back side
Kick ass simple black and gold or kick ass colorful

Target Market(s)

Retailers

Industry/Entity Type

Business

Contact Information for Business Card

Lofty Fern
Rooted deep in the Cascade Hollow Valley
Email loftyfernllc@pinemail.net

Font styles to use
Other font styles liked:
• What the artist thinks

Colors

Designer to choose colors to be used in the design.

Requirements
Must have
• Nice to look at . Like that bottle of wine you buy because the label graphics told you too.
Nice to have
• It's in my description
• You can lookup the Tarvelle Logde in Stevenson Wa and check out there logo, and I'm always up for ideas.
• Color and fonts should be what the artist thinks best
Should not have
• Boring

```html
<!DOCTYPE html>
<html lang="en">
<head>
<meta charset="utf-8">
<title>Lofty Fern – Business Cards</title>
<link rel="stylesheet" href="https://fonts.googleapis.com/css2?family=Open+Sans:wght@400;600&display=swap">
<style>
  :root {
    --backdrop: #d9d6d0;
    --card-dark: #0a0a0a;
    --card-light: #262626;
    --fern-green: #33c24d;
    --sun-orange: #f2a319;
    --text-font: "Open Sans", sans-serif;
  }
  * { box-sizing: border-box; margin: 0; padding: 0; }
  html, body {
    width: 1200px;
    height: 1000px;
    overflow: hidden;
    background: var(--backdrop);
    font-family: var(--text-font);
  }
  .canvas {
    position: relative;
    width: 1200px;
    height: 1000px;
  }
  .card {
    position: absolute;
    left: 250px;
    width: 700px;
    height: 400px;
    background: linear-gradient(135deg, var(--card-dark) 0%, var(--card-dark) 45%, var(--card-light) 100%);
    border-radius: 4px;
    box-shadow: 0 6px 18px rgba(0, 0, 0, 0.25);
  }
  .card--front { top: 70px; }
  .card--back { top: 530px; }

  .brand {
    position: absolute;
    left: 0;
    right: 0;
    display: flex;
    flex-direction: column;
    align-items: center;
  }
  .card--front .brand { top: 110px; }
  .card--back .brand { top: 70px; }

  .brand__name {
    display: flex;
    align-items: center;
    gap: 14px;
    color: var(--fern-green);
    font-weight: 400;
    font-size: 58px;
    line-height: 1;
  }
  .brand__dot {
    width: 34px;
    height: 34px;
    border-radius: 50%;
    background: var(--sun-orange);
  }
  .brand__tagline {
    margin-top: 10px;
    color: var(--sun-orange);
    font-weight: 600;
    font-size: 18px;
  }

  .front-email {
    position: absolute;
    top: 280px;
    left: 0;
    right: 0;
    display: flex;
    justify-content: center;
    align-items: center;
    gap: 16px;
    color: var(--fern-green);
    font-size: 22px;
  }
  .front-email svg { width: 30px; height: 22px; }

  .identity {
    position: absolute;
    top: 265px;
    right: 410px;
    text-align: right;
    color: var(--sun-orange);
  }
  .identity__name { font-size: 32px; line-height: 1.15; }
  .identity__role { font-size: 24px; line-height: 1.2; padding-right: 10px; }

  .divider {
    position: absolute;
    top: 230px;
    left: 325px;
    width: 3px;
    height: 120px;
    background: var(--sun-orange);
  }

  .contacts {
    position: absolute;
    top: 222px;
    left: 355px;
    list-style: none;
    color: var(--sun-orange);
    font-size: 23px;
    line-height: 1.25;
  }
</style>
</head>
<body>
<main class="canvas">

  <section class="card card--front" aria-label="Card front">
    <div class="brand">
      <div class="brand__name"><span class="brand__dot"></span>Lofty Fern</div>
      <p class="brand__tagline">Rooted deep in the Cascade Hollow Valley</p>
    </div>
    <p class="front-email">
      <svg viewBox="0 0 30 22" aria-hidden="true">
        <rect x="1" y="1" width="28" height="20" fill="var(--fern-green)"/>
        <polyline points="1,1 15,12 29,1" fill="none" stroke="var(--card-dark)" stroke-width="2"/>
      </svg>
      loftyfernllc@pinemail.net
    </p>
  </section>

  <section class="card card--back" aria-label="Card back">
    <div class="brand">
      <div class="brand__name"><span class="brand__dot"></span>Lofty Fern</div>
      <p class="brand__tagline">Rooted deep in the Cascade Hollow Valley</p>
    </div>
    <div class="identity">
      <p class="identity__name">Your Name</p>
      <p class="identity__role">Position</p>
    </div>
    <span class="divider"></span>
    <ul class="contacts">
      <li>000.000.0000</li>
      <li>000.000.0000</li>
      <li>name@email.com</li>
      <li>www.website.com</li>
    </ul>
  </section>

</main>
</body>
</html>
```